Bag packaging design of sliced bread

The project is for design of line of sliced bread with different flavours. The brand of the bread will be "Valorina". The shape of the bread will be oval. The bread will be packed in a bag. I attach the layout of the bag. The bag will be closed with a plastic clip. I attach images of similar products. The idea is to have one main design and then each colour to be different type of bread like those in the images 2 and 5.

```html
<!DOCTYPE html>
<html lang="en">
<head>
<meta charset="utf-8">
<title>Valorina Multigrain Bread – Bag Band</title>
<link href="https://fonts.googleapis.com/css2?family=Montserrat:wght@500;600;700&display=swap" rel="stylesheet">
<style>
  :root {
    --backdrop: #9e9e9e;
    --red-deep: #8e1206;
    --red-bright: #c00f12;
    --wheat-gold: #f2a63a;
    --ink-white: #ffffff;
  }
  html, body {
    margin: 0;
    padding: 0;
    width: 1085px;
    height: 1200px;
    overflow: hidden;
    background: var(--backdrop);
  }
  .bag-band {
    position: absolute;
    left: 0;
    top: 0;
    width: 1085px;
    height: 1200px;
    display: block;
  }
  .band-text {
    font-family: "Montserrat", sans-serif;
  }
  .brand-name {
    font-weight: 700;
    font-size: 84px;
    fill: var(--ink-white);
    letter-spacing: -1px;
  }
  .claim {
    font-weight: 600;
    font-size: 11px;
    fill: var(--wheat-gold);
  }
  .product-type {
    font-weight: 600;
    font-size: 17px;
    fill: var(--ink-white);
    letter-spacing: 0.5px;
  }
  .net-weight {
    font-weight: 600;
    font-size: 11px;
    fill: var(--wheat-gold);
  }
</style>
</head>
<body>
<svg class="bag-band" viewBox="0 0 1085 1200" xmlns="http://www.w3.org/2000/svg">
  <!-- left deep red panel with wheat pattern area -->
  <polygon class="panel-left" points="0,514 193,514 333,687 0,687"
           fill="var(--red-deep)" role="img" aria-label="Subtle tonal wheat ear pattern on deep red"/>
  <!-- bright red accent panel -->
  <polygon class="panel-accent" points="193,514 351,514 458,687 333,687" fill="var(--red-bright)"/>
  <!-- right deep red panel with wheat pattern area -->
  <polygon class="panel-right" points="551,514 1085,514 1085,687 690,687"
           fill="var(--red-deep)" role="img" aria-label="Subtle tonal wheat ear pattern on deep red"/>

  <!-- brand name -->
  <text class="band-text brand-name" x="480" y="618" text-anchor="middle">Valorina</text>

  <!-- claims -->
  <text class="band-text claim" x="329" y="664">HIGH IN PROTEIN</text>
  <text class="band-text claim" x="349" y="677">LOWER CARBS</text>

  <text class="band-text product-type" x="463" y="676">MULTIGRAIN BREAD</text>

  <text class="band-text net-weight" x="687" y="673">NET WEIGHT 500g</text>
</svg>
</body>
</html>
```